BrivoPeak Business Card Design Project

We are looking for a modern, clean business card design for our new company. We are a consulting firm focused on the financial services market providing management and IT consulting to banks, insurance companies, etc. Please include our company logo and company contact information from the attached file in the design. Two versions of the logo are attached, either version is acceptable. Logos are available in other file formats if needed. We would like to include the contact information for both our UK and US offices as well as the following information for each individual card holder: Name, position/title, address, phone number and e-mail address.
Updates
Project Deadline Extended
Reason: A last minute trip over seas has prevented us from finalizing the decision. A decision will be made this week. We apologize for the inconvenience.
Industry/Entity Type
Business
Contact Information for Business Card
Company logo.
Company locations and phone numbers for both the US and UK offices.
Company URL.
Cardholder Name
Cardholder Position/title
Cardholder Address
Cardholder Phone Number
Cardholder e-mail Address
Look and feel
Each slider illustrates characteristics of the customer's brand and the style your logo design should communicate.

```html
<!DOCTYPE html>
<html lang="en">
<head>
<meta charset="utf-8">
<title>BrivoPeak Partners — Business Card</title>
<link rel="stylesheet" href="https://fonts.googleapis.com/css2?family=Source+Sans+3:wght@400;600;700&display=swap">
<style>
  :root {
    --navy: #112b52;
    --slate: #5f5f5f;
    --paper: #ffffff;
    --ink: #1a2f55;
    --backdrop: #ecebe8;
  }
  * { box-sizing: border-box; margin: 0; padding: 0; }
  html, body { width: 1200px; height: 900px; overflow: hidden; }
  body {
    position: relative;
    background: var(--backdrop);
    font-family: "Source Sans 3", "Helvetica Neue", Arial, sans-serif;
  }
  .card {
    position: absolute;
    box-shadow: 0 6px 18px rgba(0,0,0,0.18);
    overflow: hidden;
  }
  /* Front */
  .card-front {
    left: 238px; top: 62px; width: 555px; height: 343px;
    background: var(--slate);
  }
  .front-panel {
    position: absolute; left: 0; top: 0; width: 395px; height: 100%;
    background: var(--navy);
  }
  .front-divider {
    position: absolute; left: 395px; top: 0; width: 6px; height: 100%;
    background: var(--paper);
  }
  .front-brand {
    position: absolute; left: 34px; top: 38px; width: 282px;
    color: var(--paper); font-weight: 700; text-align: center;
    line-height: 1;
  }
  .front-brand .brand-name { display: block; font-size: 54px; letter-spacing: -0.5px; }
  .front-brand .brand-sub { display: block; font-size: 25px; letter-spacing: 1.5px; margin-top: 6px; }
  .holder {
    position: absolute; left: 30px; top: 166px; color: var(--paper);
  }
  .holder-name { font-size: 19px; font-weight: 600; line-height: 24px; }
  .holder-title { font-size: 16px; font-weight: 400; line-height: 22px; }
  .contact-list { list-style: none; margin-top: 10px; font-size: 15.5px; line-height: 23px; }
  .contact-list li { display: flex; align-items: center; }
  .contact-list .label { display: inline-block; width: 36px; }
  .contact-list svg { width: 12px; height: 12px; margin-right: 12px; fill: var(--paper); }
  /* Back */
  .card-back {
    left: 457px; top: 518px; width: 560px; height: 344px;
    background: var(--paper);
    text-align: center; color: var(--ink);
  }
  .back-brand {
    position: absolute; left: 0; right: 0; top: 142px;
    color: var(--navy); font-weight: 700; line-height: 1;
  }
  .back-brand .brand-name { display: block; font-size: 48px; letter-spacing: -0.3px; }
  .back-brand .brand-sub { display: block; font-size: 22px; letter-spacing: 1.5px; margin-top: 4px; }
  .offices { position: absolute; left: 0; right: 0; top: 249px; font-size: 15.5px; line-height: 21px; }
  .office + .office { margin-top: 11px; }
</style>
</head>
<body>
  <section class="card card-front" aria-label="Business card front">
    <div class="front-panel"></div>
    <div class="front-divider"></div>
    <div class="front-brand">
      <span class="brand-name">BrivoPeak</span>
      <span class="brand-sub">PARTNERS</span>
    </div>
    <div class="holder">
      <p class="holder-name">Daniel Harlow</p>
      <p class="holder-title">Managing Director</p>
      <ul class="contact-list">
        <li><span class="label">US :</span>(555) 014-2276</li>
        <li><span class="label">UK :</span>+44 7700 900417</li>
        <li><svg viewBox="0 0 12 12" aria-hidden="true"><path d="M1 2.5h10v7H1z M1 2.5l5 4 5-4" fill="none" stroke="#fff" stroke-width="1.2"/></svg>info@brivopeakpartners.com</li>
        <li><svg viewBox="0 0 12 12" aria-hidden="true"><circle cx="6" cy="6" r="5.5"/></svg>www.brivopeakpartners.com</li>
      </ul>
    </div>
  </section>

  <section class="card card-back" aria-label="Business card back">
    <div class="back-brand">
      <span class="brand-name">BrivoPeak</span>
      <span class="brand-sub">PARTNERS</span>
    </div>
    <div class="offices">
      <p class="office">418 N Maple Ave, Suite 204-117<br>Brookdale UT 84102 United States</p>
      <p class="office">14-16 Carrow Street London N4 2PX Great Britain</p>
    </div>
  </section>
</body>
</html>
```